Automotive eCommerce Business looking for a business card design

Looking for a clean and simple business card design. Our company name is "Tundra Motors" and we are a company specializing in the ecommerce sales of automotive parts, specifically for pick up trucks and large SUVs. Our company colours are red, black, and white.

Feel free to use the logo provided or create a new logo that you seem fit. Looking forward to your creative ideas!

Industry/Entity Type

Automotive

Contact Information for Business Card

We were thinking of a possibly two-sided design featuring just the logo and company name on one side, and personal information on the other side. Single sided designs will be considered as well.

Font styles to use
Serif
Sans Serif
Decorative

Colors
ec1f27
ffffff
000000

Requirements
Must have
• Space for employee's name, title, phone number and email address, along with the company address and website somewhere.

```html
<!DOCTYPE html>
<html lang="en">
<head>
<meta charset="UTF-8">
<title>Tundra Motors – Business Card</title>
<link rel="stylesheet" href="https://fonts.googleapis.com/css2?family=Rubik:wght@300;400;500&display=swap">
<style>
  :root {
    --brand-red: #9b1b20;
    --ink: #111111;
    --paper: #ffffff;
    --blush: #f4e4e5;
    --rule: #8a8a8a;
    --stage: #eeeeef;
  }
  * { margin: 0; padding: 0; box-sizing: border-box; }
  html, body { width: 1200px; height: 750px; overflow: hidden; }
  body {
    background: var(--stage);
    font-family: "Rubik", Arial, sans-serif;
    position: relative;
  }
  .card {
    position: absolute;
    top: 225px;
    width: 520px;
    height: 300px;
    border-radius: 26px;
    overflow: hidden;
    box-shadow: 0 10px 28px rgba(0,0,0,0.18);
  }

  /* Front side */
  .card-front {
    left: 50px;
    background: var(--brand-red);
    color: var(--paper);
  }
  .front-brand {
    position: absolute;
    top: 112px;
    left: 0; right: 0;
    display: flex;
    align-items: center;
    justify-content: center;
    gap: 14px;
    font-size: 36px;
    font-weight: 500;
    letter-spacing: 0.5px;
  }
  .brand-dot {
    width: 18px; height: 18px;
    border-radius: 50%;
    background: var(--paper);
  }
  .front-web {
    position: absolute;
    bottom: 34px;
    left: 0; right: 0;
    text-align: center;
    font-size: 15px;
    font-weight: 400;
    letter-spacing: 0.3px;
  }

  /* Back side */
  .card-back {
    left: 630px;
    background: var(--paper);
  }
  .back-brand {
    position: absolute;
    left: 28px;
    top: 180px;
    display: flex;
    align-items: center;
    gap: 10px;
    color: var(--brand-red);
    font-size: 24px;
    font-weight: 500;
  }
  .back-brand .brand-dot { background: var(--brand-red); width: 14px; height: 14px; }
  .info-panel {
    position: absolute;
    top: -20px;
    right: -20px;
    width: 300px;
    height: 220px;
    border-radius: 40px;
    background: var(--blush);
  }
  .details {
    position: absolute;
    top: 40px;
    left: 250px;
    width: 250px;
  }
  .person-name {
    font-size: 28px;
    font-weight: 500;
    color: var(--ink);
    line-height: 1;
  }
  .person-name .surname { color: var(--brand-red); font-weight: 400; }
  .person-title {
    font-size: 18px;
    font-weight: 300;
    color: var(--brand-red);
    margin-top: 4px;
  }
  .divider {
    height: 1px;
    background: var(--rule);
    margin: 12px 0 14px;
  }
  .contact-list { list-style: none; }
  .contact-item {
    display: flex;
    align-items: flex-start;
    gap: 10px;
    font-size: 12.5px;
    color: var(--ink);
    line-height: 1.2;
    margin-bottom: 9px;
  }
  .contact-icon { width: 14px; height: 14px; flex: none; fill: var(--brand-red); }
</style>
</head>
<body>

  <section class="card card-front" aria-label="Business card front">
    <div class="front-brand"><span class="brand-dot"></span>Tundra Motors</div>
    <p class="front-web">www.tundraparts.net</p>
  </section>

  <section class="card card-back" aria-label="Business card back">
    <div class="info-panel"></div>
    <div class="back-brand"><span class="brand-dot"></span>Tundra Motors</div>

    <div class="details">
      <h1 class="person-name">Daniel <span class="surname">Reyes</span></h1>
      <p class="person-title">Web Designer</p>
      <div class="divider"></div>
      <ul class="contact-list">
        <li class="contact-item">
          <svg class="contact-icon" viewBox="0 0 24 24" aria-hidden="true"><path d="M6.6 10.8c1.4 2.8 3.8 5.1 6.6 6.6l2.2-2.2c.3-.3.7-.4 1-.2 1.1.4 2.3.6 3.6.6.6 0 1 .4 1 1V20c0 .6-.4 1-1 1C10.6 21 3 13.4 3 4c0-.6.4-1 1-1h3.5c.6 0 1 .4 1 1 0 1.3.2 2.5.6 3.6.1.3 0 .7-.2 1L6.6 10.8z"/></svg>
          +15550142298
        </li>
        <li class="contact-item">
          <svg class="contact-icon" viewBox="0 0 24 24" aria-hidden="true"><path d="M2 5h20v14H2z M3.5 6.5 12 13l8.5-6.5" fill="var(--brand-red)" stroke="#fff" stroke-width="1.5"/></svg>
          reyes@tundraparts.net
        </li>
        <li class="contact-item">
          <svg class="contact-icon" viewBox="0 0 24 24" aria-hidden="true"><circle cx="12" cy="12" r="9" fill="none" stroke="var(--brand-red)" stroke-width="2"/><path d="M3 12h18M12 3c3 3 3 15 0 18M12 3c-3 3-3 15 0 18" fill="none" stroke="var(--brand-red)" stroke-width="1.6"/></svg>
          www.tundraparts.net
        </li>
        <li class="contact-item">
          <svg class="contact-icon" viewBox="0 0 24 24" aria-hidden="true"><path d="M12 2a7 7 0 0 0-7 7c0 5 7 13 7 13s7-8 7-13a7 7 0 0 0-7-7zm0 9.5a2.5 2.5 0 1 1 0-5 2.5 2.5 0 0 1 0 5z"/></svg>
          <span>Ridgeway Ave. Northfield D.<br>48210 pk. Millbrook</span>
        </li>
      </ul>
    </div>
  </section>

</body>
</html>
```